Halvorsen Business Card

This is the personal business card for Dr Mark Halvorsen and convers three area of his professional activity - all of them involve (foreign) languages:
o QRBW International Ltd - A translation company with 50 staff. Trades internationally
o WideHarbor Ltd - a global online auction marketplace for translation services (startup)
o Vocal Thread - cutting edge technology from the brain sciences which helps learners assimilate the sound patterns of a new language (startup)

Target Market(s)

The card needs to have a "cutting edge" feel - but for a fairly conservative audience - academics, investors.

Industry/Entity Type

Business

Requirements
Must have
• Text:
Dr Mark Halvorsen

Co-founder QRBW International Ltd (Language translation)
Founder WideHarbor Ltd (Translation marketplace)
Founder Vocal Thread (Language acquisition)

email: mark.tolvin@quandamail.co.nz
Phone: +64 21 593 4162
Twitter: @MarkTolvin7

```html
<!DOCTYPE html>
<html lang="en">
<head>
<meta charset="utf-8">
<title>Halvorsen Business Card</title>
<link rel="stylesheet" href="https://fonts.googleapis.com/css2?family=Parisienne&family=Crimson+Text:wght@400&display=swap">
<style>
  :root {
    --backdrop: #4a4848;
    --card: #66352f;
    --gold: #f3dc7c;
    --gold-glow: rgba(255, 236, 150, 0.55);
    --label: #e6c766;
    --ink: #f1e7dc;
  }
  * { margin: 0; padding: 0; box-sizing: border-box; }
  html, body {
    width: 1200px;
    height: 534px;
    overflow: hidden;
    background: var(--backdrop);
  }
  .stage {
    position: relative;
    width: 1200px;
    height: 534px;
  }
  .card {
    position: absolute;
    top: 119px;
    width: 518px;
    height: 295px;
    background: var(--card);
    font-family: "Crimson Text", Georgia, serif;
    color: var(--ink);
  }
  .card--square { left: 62px; }
  .card--rounded { left: 622px; border-radius: 16px; }
  .card__name {
    position: absolute;
    left: 36px;
    top: 38px;
    font-family: "Parisienne", cursive;
    font-weight: 400;
    font-size: 56px;
    line-height: 1;
    color: var(--gold);
    white-space: nowrap;
    text-shadow: 0 0 3px var(--gold-glow), 0 0 8px var(--gold-glow);
  }
  .card__contact,
  .card__ventures {
    position: absolute;
    left: 48px;
    list-style: none;
    font-size: 13px;
    line-height: 17px;
    white-space: nowrap;
  }
  .card__contact { top: 142px; }
  .card__ventures { top: 209px; }
  .label, .company { color: var(--label); }
</style>
</head>
<body>
<main class="stage">
  <article class="card card--square">
    <h1 class="card__name">Dr Mark Halvorsen</h1>
    <ul class="card__contact">
      <li><span class="label">Email:</span> mark.tolvin@quandamail.co.nz</li>
      <li><span class="label">Phone:</span> +64 21 593 4162</li>
      <li><span class="label">Twitter:</span> @MarkTolvin7</li>
    </ul>
    <ul class="card__ventures">
      <li>Co-founder <span class="company">QRBW International Ltd</span> (Language translation)</li>
      <li>Founder <span class="company">WideHarbor Ltd</span> (Translation marketplace)</li>
      <li>Founder <span class="company">Vocal Thread</span> (Language acquisition)</li>
    </ul>
  </article>

  <article class="card card--rounded">
    <h1 class="card__name">Dr Mark Halvorsen</h1>
    <ul class="card__contact">
      <li><span class="label">Email:</span> mark.tolvin@quandamail.co.nz</li>
      <li><span class="label">Phone:</span> +64 21 593 4162</li>
      <li><span class="label">Twitter:</span> @MarkTolvin7</li>
    </ul>
    <ul class="card__ventures">
      <li>Co-founder <span class="company">QRBW International Ltd</span> (Language translation)</li>
      <li>Founder <span class="company">WideHarbor Ltd</span> (Translation marketplace)</li>
      <li>Founder <span class="company">Vocal Thread</span> (Language acquisition)</li>
    </ul>
  </article>
</main>
</body>
</html>
```